Marcus Lindqvist Photography needs a business card designs

I am looking for a business card with a logo clean and simple which I can use that logo on my website or on my pictures. It has to be very classy and very professional. Please look at my website at www.marcuslvqphoto.com for my signature. I'm thinking of something like that for my signature/logo. I'm still working on my website but you get an idea. I'm open to any design but not too busy graphics.

I will be printing the business card from qrivel.com.

Surprise me :)

contact me if you have any questions.

-ML

I'm receiving a lot of black background at the moment. I know my website is all black doesn't mean I want my card to be all black. Please send in with some white background as well. Thanks :)

check out some business cards that I found online. I think they are simple and look really awesome. I don't want a card that is too busy.

http://www.marcuslvqphoto.com/p270092084

Reason: Please extend the date for me. I haven't really receive any good design yet.

Printing

• -a logo that related to my first and last initial of my name "ML"
-double sided
• -I don't want my background to be all black.
-no pictures on the card

```html
<!DOCTYPE html>
<html lang="en">
<head>
<meta charset="utf-8">
<title>Marcus Lindqvist Photography – Business Card</title>
<link rel="stylesheet" href="https://fonts.googleapis.com/css2?family=Josefin+Sans:wght@100&family=Open+Sans:wght@300&family=Cutive+Mono&display=swap">
<style>
  :root {
    --backdrop: #1c1c1c;
    --card: #ffffff;
    --ink: #111111;
    --ink-soft: #555555;
    --ink-mid: #333333;
  }
  * { margin: 0; padding: 0; box-sizing: border-box; }
  html, body {
    width: 1134px;
    height: 1200px;
    overflow: hidden;
    background: var(--backdrop);
  }
  .stage {
    position: relative;
    width: 1134px;
    height: 1200px;
  }
  .card {
    position: absolute;
    width: 669px;
    height: 382px;
    background: var(--card);
    overflow: hidden;
  }
  .card--back { left: 218px; top: 202px; }
  .card--front { left: 220px; top: 607px; }

  .contact {
    position: absolute;
    font-family: "Open Sans", Arial, sans-serif;
    font-weight: 300;
    font-size: 18px;
    line-height: 1;
    letter-spacing: 0.5px;
    color: var(--ink-soft);
    white-space: nowrap;
  }
  .contact--email { left: 70px; top: 111px; }
  .contact--phone { left: 85px; top: 275px; letter-spacing: 2px; color: var(--ink-mid); }
  .contact--web { right: 36px; top: 227px; color: var(--ink-mid); }

  .monogram {
    position: absolute;
    font-family: "Josefin Sans", Helvetica, sans-serif;
    font-weight: 100;
    font-size: 66px;
    line-height: 1;
    color: var(--ink);
    letter-spacing: -2px;
  }
  .card--back .monogram { right: 20px; bottom: 3px; }
  .card--front .monogram { left: 18px; bottom: 2px; }

  .holder-name {
    position: absolute;
    right: 40px;
    top: 104px;
    font-family: "Cutive Mono", "Courier New", monospace;
    font-weight: 400;
    font-size: 26px;
    line-height: 1;
    letter-spacing: 1px;
    color: var(--ink);
    white-space: nowrap;
  }
</style>
</head>
<body>
  <main class="stage">
    <section class="card card--back" aria-label="Card back">
      <p class="contact contact--email">info@marcuslvqphoto.com</p>
      <p class="contact contact--phone">1-877-555-0142</p>
      <span class="monogram">ML</span>
    </section>

    <section class="card card--front" aria-label="Card front">
      <h1 class="holder-name">Marcus Lindqvist</h1>
      <p class="contact contact--web">www.marcuslvqphoto.com</p>
      <span class="monogram">ML</span>
    </section>
  </main>
</body>
</html>
```